Banner/Werbemittel für Lesebrillen Shop
Zielgruppe
Es handelt sich um einen Online-Shop für Lesebrillen, die innerhalb von Deutschland verkauft werden. Die Zielgruppe ist daher eher etwas älter (45+).
Aufgabenstellung
Bitte erstellen Sie uns Werbebanner für unser Image- und Retargeting Programm. Diese Banner sollen an die Webseite www.lirafensa.de angelehnt sein.
Wichtige Vorteile die angegeben werden können:
- Kostenloser Versand & Rückversand
- 30 Tage erweitertes Rückgaberecht
- Kauf auf Rechnung
Die Banner werden in den folgenden Größen benötigt:
728x90
300x250
120x600
320x50
Das Logo habe ich beigefügt. Sollten Sie weitere Bilder benötigen, können Sie sich gerne auf der Webseite bedienen.

```html
<!DOCTYPE html>
<html lang="de">
<head>
<meta charset="utf-8">
<title>Lirafensa – Werbebanner</title>
<link href="https://fonts.googleapis.com/css2?family=Open+Sans:wght@400;600&display=swap" rel="stylesheet">
<style>
  :root {
    --teal: #7ccac1;
    --teal-dark: #6bbfb5;
    --brand: #3d8fc4;
    --text: #6b6b6b;
    --tick: #8dc63f;
    --line: #dcdcdc;
    --page: #ffffff;
    --photo-light: #e9e9e9;
    --photo-mid: #b9b9b9;
    --photo-dark: #8a8a8a;
  }
  * { box-sizing: border-box; margin: 0; padding: 0; }
  html, body { width: 1178px; height: 1200px; overflow: hidden; background: var(--page); }
  body { position: relative; font-family: "Open Sans", Arial, sans-serif; color: var(--text); }

  .banner { position: absolute; background: #fff; border: 1px solid var(--line); overflow: hidden; }
  .brand-name { color: var(--brand); font-weight: 400; letter-spacing: -0.5px; line-height: 1; }
  .claim { line-height: 1.3; }
  .cta {
    position: absolute; display: flex; align-items: center; justify-content: center; text-align: center;
    background: var(--teal); color: #fff; font-weight: 600; line-height: 1.3;
  }
  .benefits { position: absolute; list-style: none; }
  .benefits li { position: relative; line-height: 1.2; }
  .benefits svg { position: absolute; left: 0; }
  .photo {
    position: absolute;
    background: linear-gradient(90deg, var(--photo-light) 0%, var(--photo-mid) 45%, var(--photo-dark) 60%, var(--photo-light) 100%);
  }

  /* 728 x 90 */
  .leaderboard { left: 125px; top: 113px; width: 1014px; height: 125px; }
  .leaderboard .side-bar { position: absolute; left: 0; top: 0; width: 18px; height: 100%; background: var(--teal); }
  .leaderboard .brand-name { position: absolute; left: 40px; top: 24px; font-size: 38px; }
  .leaderboard .claim { position: absolute; left: 40px; top: 70px; font-size: 17px; }
  .leaderboard .photo { left: 300px; top: 0; width: 320px; height: 100%;
    background: linear-gradient(90deg, #fff 0%, var(--photo-light) 20%, var(--photo-mid) 50%, var(--photo-dark) 65%, var(--photo-light) 90%, #fff 100%); }
  .leaderboard .cta { left: 508px; top: 38px; width: 126px; height: 42px; font-size: 15px; }
  .leaderboard .benefits { left: 700px; top: 10px; font-size: 15px; }
  .leaderboard .benefits li { padding-left: 30px; margin-bottom: 6px; }
  .leaderboard .benefits svg { top: -2px; width: 22px; height: 20px; }

  /* 300 x 250 */
  .rectangle { left: 125px; top: 321px; width: 382px; height: 319px; }
  .rectangle .top-band { position: absolute; left: 0; top: 0; width: 100%; height: 20px; background: var(--teal); }
  .rectangle .photo { left: 170px; top: 20px; width: 212px; height: 299px; }
  .rectangle .brand-name { position: absolute; left: 16px; top: 42px; font-size: 38px; }
  .rectangle .claim { position: absolute; left: 16px; top: 94px; font-size: 17px; }
  .rectangle .benefits { left: 14px; top: 176px; font-size: 15px; }
  .rectangle .benefits li { padding-left: 32px; margin-bottom: 8px; }
  .rectangle .benefits svg { top: -4px; width: 24px; height: 22px; }
  .rectangle .cta { left: 215px; top: 258px; width: 160px; height: 44px; font-size: 15px; }

  /* 120 x 600 */
  .skyscraper { left: 623px; top: 321px; width: 154px; height: 770px; }
  .skyscraper .top-band { position: absolute; left: 0; top: 0; width: 100%; height: 20px; background: var(--teal); }
  .skyscraper .brand-name { position: absolute; left: 14px; top: 44px; font-size: 30px; }
  .skyscraper .claim { position: absolute; left: 14px; top: 88px; font-size: 17px; }
  .skyscraper .photo { left: 0; top: 235px; width: 154px; height: 240px; }
  .skyscraper .benefits { left: 12px; top: 488px; font-size: 15px; }
  .skyscraper .benefits li { padding-left: 30px; margin-bottom: 10px; }
  .skyscraper .benefits svg { top: -4px; width: 22px; height: 20px; }
  .skyscraper .cta { left: 19px; top: 668px; width: 116px; height: 64px; font-size: 15px; }

  /* 320 x 50 */
  .mobile { left: 125px; top: 724px; width: 410px; height: 64px; }
  .mobile .side-bar { position: absolute; left: 0; top: 0; width: 16px; height: 100%; background: var(--teal); }
  .mobile .brand-name { position: absolute; left: 40px; top: 17px; font-size: 28px; }
  .mobile .claim { position: absolute; left: 190px; top: 14px; font-size: 13px; }
</style>
</head>
<body>

<svg width="0" height="0" style="position:absolute">
  <symbol id="tick" viewBox="0 0 24 22">
    <path d="M2 12 L9 19 L22 3" fill="none" stroke="var(--tick)" stroke-width="3.5" stroke-linecap="round" stroke-linejoin="round"/>
  </symbol>
</svg>

<section class="banner leaderboard" aria-label="Banner 728 x 90">
  <div class="side-bar"></div>
  <p class="brand-name">Lirafensa</p>
  <p class="claim">Lesebrillen sicher &amp; bequem<br>online bestellen!</p>
  <div class="photo" role="img" aria-label="Foto: Mann mit Lesebrille, halb farbig, halb schwarzweiß"></div>
  <div class="cta">Jetzt entdecken</div>
  <ul class="benefits">
    <li><svg><use href="#tick"/></svg>Kostenloser Versand</li>
    <li><svg><use href="#tick"/></svg>30 Tage erweitertes<br>Rückgaberecht</li>
    <li><svg><use href="#tick"/></svg>Kauf auf Rechnung</li>
  </ul>
</section>

<section class="banner rectangle" aria-label="Banner 300 x 250">
  <div class="top-band"></div>
  <div class="photo" role="img" aria-label="Foto: Mann mit Lesebrille, halb farbig, halb schwarzweiß"></div>
  <p class="brand-name">Lirafensa</p>
  <p class="claim">Lesebrillen<br>sicher &amp; bequem<br>online bestellen!</p>
  <ul class="benefits">
    <li><svg><use href="#tick"/></svg>Kostenloser Versand</li>
    <li><svg><use href="#tick"/></svg>30 Tage erw.<br>Rückgaberecht</li>
    <li><svg><use href="#tick"/></svg>Kauf auf Rechnung</li>
  </ul>
  <div class="cta">Jetzt entdecken</div>
</section>

<section class="banner skyscraper" aria-label="Banner 120 x 600">
  <div class="top-band"></div>
  <p class="brand-name">Lirafensa</p>
  <p class="claim">Lesebrillen<br>sicher &amp;<br>bequem<br>online<br>bestellen!</p>
  <div class="photo" role="img" aria-label="Foto: Mann mit Lesebrille, halb farbig, halb schwarzweiß"></div>
  <ul class="benefits">
    <li><svg><use href="#tick"/></svg>Kostenloser<br>Versand</li>
    <li><svg><use href="#tick"/></svg>30 Tage<br>erw. Rück-<br>gaberecht</li>
    <li><svg><use href="#tick"/></svg>Kauf auf<br>Rechnung</li>
  </ul>
  <div class="cta">Jetzt<br>entdecken</div>
</section>

<section class="banner mobile" aria-label="Banner 320 x 50">
  <div class="side-bar"></div>
  <p class="brand-name">Lirafensa</p>
  <p class="claim">Lesebrillen sicher &amp; bequem<br>online bestellen!</p>
</section>

</body>
</html>
```